High Performance Webhosting Plimbo ad Banners

We are looking for a designer that can design some very high quality and eye catching animated gif ad banners in several size and shapes to suit standards for Plimbo ads.
* leaderboard (728x90)
* banner (468x60)
* half banner (234x60)
* button (125x125)
* skyscraper (120x600)
* wide skyscraper (160x600)
* small rectangle (180x150)
* vertical banner (120 x 240)

The message we want to put out on these banners is as follows:

High Performance Australian Velkora Web Hosting
VPS with SSD's
Velkora Speed Optmisation also available
The company Name is "Quomplin"
I have attached the logo and the URL: www.quomplin.com.au

Target Market(s)

Velkora webhosting, Ecommerce Webhosting

Industry/Entity Type

Plimbo

Font styles to use
Sans Serif

Colors
33a6d7
0692cd
85cae6
0556a4
3176b5
cedeed

Requirements
Must have
• High quality design with animated gif if possible to catch eye.
Nice to have
• Animated gif to be more affective in getting attention.
Should not have
• No prices to be displayed.

```html
<!DOCTYPE html>
<html lang="en">
<head>
<meta charset="utf-8">
<title>Quomplin Banner Set</title>
<link href="https://fonts.googleapis.com/css2?family=Arimo:wght@400;700&display=swap" rel="stylesheet">
<style>
  :root {
    --blue-bright: #33a6d7;
    --blue-mid: #0692cd;
    --blue-light: #85cae6;
    --blue-deep: #0556a4;
    --blue-steel: #3176b5;
    --blue-pale: #cedeed;
    --logo-blue: #1e9be0;
    --orange: #f7a33c;
    --orange-dark: #d9751a;
    --brown: #6b3a12;
    --grey: #8c8f94;
    --ink: #222222;
    --page: #ffffff;
  }
  * { margin: 0; padding: 0; box-sizing: border-box; }
  html, body {
    width: 1200px; height: 1200px; overflow: hidden;
    background: var(--page);
    font-family: "Arimo", Arial, sans-serif;
  }
  .artboard {
    position: absolute; left: 0; top: 0;
    width: 860px; height: 860px;
    transform: scale(1.3953); transform-origin: 0 0;
  }
  .banner { position: absolute; display: block; border: 1px solid #9a9a9a; }
  .banner--leaderboard { left: 75px; top: 35px; width: 728px; height: 90px; }
  .banner--skyscraper { left: 376px; top: 189px; width: 160px; height: 600px; }
  .size-label {
    position: absolute; width: 200px; left: 355px;
    text-align: center; font-size: 14px; color: var(--ink);
  }
  .size-label--leaderboard { top: 139px; }
  .size-label--skyscraper { top: 800px; }
  .headline { font-family: "Arimo", Arial, sans-serif; font-weight: 700; fill: #fff; }
  .brand { font-family: "Arimo", Arial, sans-serif; font-weight: 700; fill: var(--logo-blue); }
  .url { font-family: "Arimo", Arial, sans-serif; fill: #fff; }
  .cta-text { font-family: "Arimo", Arial, sans-serif; font-weight: 700; fill: #fff; }
</style>
</head>
<body>
<main class="artboard">

  <svg class="banner banner--leaderboard" viewBox="0 0 728 90" xmlns="http://www.w3.org/2000/svg">
    <defs>
      <linearGradient id="lbBlue" x1="0" y1="0" x2="0" y2="1">
        <stop offset="0" stop-color="var(--blue-steel)"/>
        <stop offset="1" stop-color="var(--blue-deep)"/>
      </linearGradient>
      <linearGradient id="lbPanel" x1="0" y1="0" x2="1" y2="1">
        <stop offset="0" stop-color="var(--blue-bright)"/>
        <stop offset="1" stop-color="var(--blue-mid)"/>
      </linearGradient>
      <linearGradient id="lbLogo" x1="0" y1="0" x2="0" y2="1">
        <stop offset="0" stop-color="#ffffff"/>
        <stop offset="1" stop-color="#e4e6e9"/>
      </linearGradient>
      <linearGradient id="lbPhoto" x1="0" y1="0" x2="1" y2="1">
        <stop offset="0" stop-color="#b9d9ef"/>
        <stop offset="0.6" stop-color="#8c96a3"/>
        <stop offset="1" stop-color="#4d5560"/>
      </linearGradient>
      <linearGradient id="lbCta" x1="0" y1="0" x2="0" y2="1">
        <stop offset="0" stop-color="#fbc06a"/>
        <stop offset="1" stop-color="var(--orange)"/>
      </linearGradient>
    </defs>
    <rect class="background" width="728" height="90" fill="url(#lbBlue)"/>
    <path class="logo-area" d="M0 0 H160 Q182 45 160 90 H0 Z" fill="url(#lbLogo)"/>
    <path class="logo-edge" d="M162 0 Q184 45 162 90" fill="none" stroke="var(--blue-light)" stroke-width="3"/>
    <text class="brand" x="80" y="54" font-size="28" text-anchor="middle">Quomplin</text>

    <polygon class="message-panel" points="250,3 475,3 462,87 232,87" fill="url(#lbPanel)" stroke="var(--blue-light)" stroke-width="1"/>
    <text class="headline" x="355" y="19" font-size="16" text-anchor="middle">HIGH PERFOMANCE</text>
    <text class="headline" x="355" y="36" font-size="16" text-anchor="middle">AUSTRALIAN</text>
    <text class="headline" x="355" y="53" font-size="16" text-anchor="middle">VELKORA</text>
    <text class="headline" x="355" y="70" font-size="16" text-anchor="middle">WEBHOSTING</text>
    <text class="url" x="375" y="83" font-size="9" text-anchor="middle">www.quomplin.com.au</text>

    <rect class="photo" x="522" y="0" width="206" height="90" fill="url(#lbPhoto)" role="img" aria-label="Photo of a smiling businessman beside server racks under a blue sky"/>
    <polygon class="divider-chevron" points="512,0 528,0 518,45 528,90 512,90 504,45" fill="var(--grey)"/>

    <g class="cta">
      <rect x="593" y="31" width="127" height="35" rx="3" fill="url(#lbCta)" stroke="var(--orange-dark)"/>
      <rect x="684" y="31" width="36" height="35" rx="3" fill="var(--orange-dark)"/>
      <text class="cta-text" x="638" y="53" font-size="13" text-anchor="middle">Click Here</text>
      <circle cx="702" cy="48.5" r="11" fill="var(--brown)" stroke="#f3d2a3" stroke-width="1.5"/>
      <polygon points="698,42 708,48.5 698,55" fill="#fff"/>
    </g>
  </svg>
  <p class="size-label size-label--leaderboard">728X90</p>

  <svg class="banner banner--skyscraper" viewBox="0 0 160 600" xmlns="http://www.w3.org/2000/svg">
    <defs>
      <linearGradient id="skBlue" x1="0" y1="0" x2="0" y2="1">
        <stop offset="0" stop-color="var(--blue-steel)"/>
        <stop offset="1" stop-color="var(--blue-deep)"/>
      </linearGradient>
      <linearGradient id="skPanel" x1="0" y1="0" x2="1" y2="1">
        <stop offset="0" stop-color="var(--blue-bright)"/>
        <stop offset="1" stop-color="var(--blue-mid)"/>
      </linearGradient>
      <linearGradient id="skLogo" x1="0" y1="0" x2="0" y2="1">
        <stop offset="0" stop-color="#ffffff"/>
        <stop offset="1" stop-color="#e2e4e7"/>
      </linearGradient>
      <linearGradient id="skPhoto" x1="0" y1="0" x2="1" y2="1">
        <stop offset="0" stop-color="#c3def1"/>
        <stop offset="0.55" stop-color="#9aa3ad"/>
        <stop offset="1" stop-color="#4d5560"/>
      </linearGradient>
      <linearGradient id="skCta" x1="0" y1="0" x2="0" y2="1">
        <stop offset="0" stop-color="#fbc06a"/>
        <stop offset="1" stop-color="var(--orange)"/>
      </linearGradient>
    </defs>
    <rect class="background" width="160" height="600" fill="url(#skBlue)"/>
    <path class="logo-area" d="M0 0 H160 V82 Q80 100 0 82 Z" fill="url(#skLogo)"/>
    <path class="logo-edge" d="M0 86 Q80 104 160 86" fill="none" stroke="var(--blue-light)" stroke-width="3"/>
    <text class="brand" x="80" y="44" font-size="27" text-anchor="middle">Quomplin</text>

    <polygon class="message-panel" points="0,162 158,108 158,293 0,356" fill="url(#skPanel)" stroke="var(--blue-light)" stroke-width="1"/>
    <text class="headline" x="80" y="184" font-size="17" text-anchor="middle">HIGH</text>
    <text class="headline" x="80" y="208" font-size="17" text-anchor="middle">PERFOMANCE</text>
    <text class="headline" x="80" y="232" font-size="17" text-anchor="middle">AUSTRALIAN</text>
    <text class="headline" x="80" y="256" font-size="17" text-anchor="middle">VELKORA</text>
    <text class="headline" x="80" y="280" font-size="17" text-anchor="middle">WEBHOSTING</text>
    <text class="url" x="80" y="364" font-size="10" text-anchor="middle">www.quomplin.com.au</text>

    <rect class="photo" x="0" y="402" width="160" height="198" fill="url(#skPhoto)" role="img" aria-label="Photo of a smiling businessman beside server racks under a blue sky"/>
    <polygon class="divider-chevron" points="0,398 80,384 160,398 160,414 80,400 0,414" fill="var(--grey)"/>

    <g class="cta">
      <rect x="14" y="550" width="132" height="35" rx="3" fill="url(#skCta)" stroke="var(--orange-dark)"/>
      <rect x="109" y="550" width="37" height="35" rx="3" fill="var(--orange-dark)"/>
      <text class="cta-text" x="61" y="572" font-size="13" text-anchor="middle">Click Here</text>
      <circle cx="127.5" cy="567.5" r="11" fill="var(--brown)" stroke="#f3d2a3" stroke-width="1.5"/>
      <polygon points="123.5,561 133.5,567.5 123.5,574" fill="#fff"/>
    </g>
  </svg>
  <p class="size-label size-label--skyscraper">160X600</p>

</main>
</body>
</html>
```